"The Quiet Mirror" Musical Theatre Poster Design

Hi there! I need a poster design for a new youth musical I'm writing called "The Quiet Mirror".

The story is about a girl called Terri who is the most popular girl in the school. However, after a horrible accident, Terri is confined to a wheelchair. Not only does she have to deal with coming to terms with her life in a wheelchair, but she also has to make new friends after her old group of friends decide that she no longer fits their idea of 'perfect'. It's a powerful, modern story that uses contemporary music, technology but also hits at the heart of the teenage social experience.

Musically, the styles include pop, RnB, and pop/rock.

As for what I need in the poster - I'm not really sure! I'm looking for something that:
- uses the title "The Quiet Mirror" in a unique way
- doesn't necessarily use a wheelchair as an image
- would appeal to a 10-15 year old audience (so not too childish, more teen or tween), yet has a sense of seriousness to it. The musical is dramatic and deals with some confronting issues.
- includes "A New Musical by Maya Fitch"

As for colours, etc. surprise me! Sorry I can't be more specific but I haven't even really got a visual on it at all.

If you would like some demo recordings of the music, just let me know!

I've also attached some poster that I really like - more of a reference point of how a musical theatre poster should look.

Target Market(s)

Teens and adults

Font styles to use
Serif
Sans Serif

Colors

Designer to choose colors to be used in the design.

Requirements
Nice to have
• * perhaps use the concept of "different" and "normal" as two opposite yet somehow similar words.
• * maybe use of circles to symbolise a wheelchair but also having to start again, circular nature of life, rebirth, renewal?
Should not have
• - not any instruments in the design. The poster is for a theatrical musical, not a pop group, or singular song.

```html
<!DOCTYPE html>
<html lang="en">
<head>
<meta charset="utf-8">
<title>The Quiet Mirror – Poster</title>
<link href="https://fonts.googleapis.com/css2?family=Permanent+Marker&display=swap" rel="stylesheet">
<style>
  :root {
    --backdrop: #eeeeef;
    --ink-white: #ffffff;
    --deep-red: #8a1a0c;
    --red-shade: #5e0f06;
    --acid-yellow: #d6d42c;
    --olive-shade: #a9a51c;
    --hot-magenta: #e23cd8;
    --magenta-shade: #a61f9c;
    --night-black: #0b0b0b;
    --violet: #8a30d2;
    --violet-light: #b45cf0;
    --stripe-black: #1e1e1e;
  }
  html, body {
    margin: 0;
    padding: 0;
    width: 981px;
    height: 1200px;
    overflow: hidden;
    background: var(--backdrop);
  }
  .poster {
    position: absolute;
    left: 85px;
    top: 30px;
    width: 810px;
    height: 1140px;
    box-shadow: 0 6px 18px rgba(0,0,0,0.25);
  }
  .poster svg { display: block; width: 100%; height: 100%; }
  .title-line {
    font-family: "Permanent Marker", cursive;
    fill: var(--ink-white);
    text-anchor: middle;
  }
  .title-word { font-size: 74px; letter-spacing: 2px; }
  .credit-line {
    font-family: "Permanent Marker", cursive;
    fill: var(--ink-white);
    text-anchor: middle;
    font-size: 27px;
    letter-spacing: 1px;
  }
  .frame { fill: none; stroke: var(--ink-white); stroke-width: 11; }
  .stripe { fill: var(--stripe-black); opacity: 0.96; }
</style>
</head>
<body>
<div class="poster">
  <svg viewBox="0 0 710 1000" preserveAspectRatio="none" xmlns="http://www.w3.org/2000/svg">
    <defs>
      <linearGradient id="redTone" x1="0" y1="0" x2="1" y2="1">
        <stop offset="0" stop-color="var(--deep-red)"/>
        <stop offset="1" stop-color="var(--red-shade)"/>
      </linearGradient>
      <linearGradient id="yellowTone" x1="0" y1="0" x2="1" y2="1">
        <stop offset="0" stop-color="var(--olive-shade)"/>
        <stop offset="0.5" stop-color="var(--acid-yellow)"/>
        <stop offset="1" stop-color="var(--olive-shade)"/>
      </linearGradient>
      <linearGradient id="magentaTone" x1="0" y1="0" x2="1" y2="1">
        <stop offset="0" stop-color="var(--magenta-shade)"/>
        <stop offset="0.6" stop-color="var(--hot-magenta)"/>
        <stop offset="1" stop-color="var(--magenta-shade)"/>
      </linearGradient>
      <linearGradient id="violetTone" x1="0" y1="0" x2="1" y2="1">
        <stop offset="0" stop-color="var(--violet)"/>
        <stop offset="0.5" stop-color="var(--violet-light)"/>
        <stop offset="1" stop-color="var(--violet)"/>
      </linearGradient>
    </defs>

    <g class="collage">
      <polygon role="img" aria-label="Toned photo panel: patterned red fabric" fill="url(#yellowTone)"
               points="0,0 710,0 710,510 0,370"/>
      <polygon role="img" aria-label="Toned photo panel: ornate red surface" fill="url(#redTone)"
               points="0,0 430,0 320,150 0,235"/>
      <polygon role="img" aria-label="Toned photo panel: dark shadowed area" fill="var(--night-black)"
               points="430,450 710,480 710,820 430,830"/>
      <polygon role="img" aria-label="Toned photo panel: magenta close-up" fill="url(#magentaTone)"
               points="0,360 450,440 430,840 0,850"/>
      <polygon role="img" aria-label="Toned photo panel: violet stage lights" fill="url(#violetTone)"
               points="0,850 430,835 710,815 710,1000 0,1000"/>
    </g>

    <g class="stripes">
      <polygon class="stripe" points="258,0 312,0 138,1000 84,1000"/>
      <polygon class="stripe" points="330,0 385,0 212,1000 157,1000"/>
      <polygon class="stripe" points="402,0 455,0 282,1000 229,1000"/>
      <polygon class="stripe" points="472,0 527,0 355,1000 300,1000"/>
      <polygon class="stripe" points="545,0 625,0 463,1000 383,1000"/>
    </g>

    <rect class="frame" x="80" y="77" width="556" height="842"/>

    <g class="title">
      <text class="title-line title-word" x="358" y="372">THE</text>
      <text class="title-line title-word" x="375" y="470">QUIET</text>
      <text class="title-line title-word" x="375" y="552">MIRROR</text>
    </g>
    <text class="credit-line" x="355" y="640">A NEW MUSICAL BY MAYA FITCH</text>
  </svg>
</div>
</body>
</html>
```